Etiketten für Rotwein
Zielgruppe
Wir starten dieses Jahr mit unserem ersten Rotwein unserer neuen Marke CAL VERDUNES aus unserem neuen Weingut auf Mallorca.
Es folgen in den kommenden Jahren ein Rosé und weitere Weißweine.
Aufgabenstellung
Wir suchen ein Design für unser erstes Flaschenetikett der Rotweinflaschen.
Die Höhe soll maximal 130 mm sein.
Der Name soll 'Bertoldo' sein.
Die Rebsorte 'Cabernet Sauvignon' und der Jahrgang '2025' sollen mit erscheinen.
Unser Logo sollte mit integriert werden.
Das Erscheinungsbild soll edel, elegant, markant, präsent, wieder erkennbar und einzigartig sein.
Es gibt ein paar Ideen, diese sind aber nur als Hinweise zu verstehen, die verwendet werden könnten.
Dies sind 2 Teddybären im Weinfeld, Teddybären auf einem Traktor im Weinfeld/ Weinberg, Landschaft oder eben komplett etwas anderes Kreatives.
Die Anlagen sind unser Logo in 3 Varianten und einige Beispiele von eigenen unprofessionellen Versuchen, sowie tolle Etikettendesigns die uns gefallen.
We are looking for a design for our first red wine bottle label.
The maximum height should be 130mm.
The name should be 'Bertoldo'.
The grape variety 'Cabernet Sauvignon' and the vintage 2025 should also be included.
Our logo should be integrated.
The overall look should be sophisticated, elegant, striking, memorable, recognizable, and unique.
We have a few ideas, but these are just suggestions that could be used.
These include two teddy bears in a vineyard, teddy bears on a tractor in a vineyard, a landscape, or something completely different and creative.
Attached are our logo in three variations, some examples of our own unprofessional attempts, and some great label designs that we like.
Jens & Uwe
Cal Verdunes

```html
<!DOCTYPE html>
<html lang="es">
<head>
<meta charset="utf-8">
<title>Bertoldo – Cabernet Sauvignon label variants</title>
<link rel="stylesheet" href="https://fonts.googleapis.com/css2?family=Cinzel:wght@600&family=Libre+Caslon+Text:wght@400&family=Lato:wght@400;700&family=Marcellus&display=swap">
<style>
  :root {
    --page-top: #ffffff;
    --page-bottom: #e4e4e7;
    --label-brown: #45200f;
    --label-brown-dark: #361608;
    --gold-light: #e6cba3;
    --gold-mid: #c8a57a;
    --gold-deep: #9c7750;
    --wine-red: #b5120f;
    --wine-red-deep: #8c0c0a;
    --title-gold: #d9bb92;
    --variety-red: #c4161a;
    --year-cream: #efe3d2;
    --ink: #1a1a1a;
    --field-ochre: #a06c36;
    --field-ochre-light: #c08a4c;
    --field-green: #7d8660;
    --sky-glow: #a8754c;
  }
  * { box-sizing: border-box; margin: 0; padding: 0; }
  html, body { width: 1200px; height: 1200px; overflow: hidden; }
  body {
    position: relative;
    background: linear-gradient(180deg, var(--page-top) 0%, var(--page-bottom) 100%);
    font-family: "Lato", sans-serif;
    color: var(--ink);
  }
  .variant-caption {
    position: absolute;
    top: 46px;
    font-size: 17px;
  }
  .variant-caption--one { left: 80px; }
  .variant-caption--two { right: 84px; }

  .label {
    position: absolute;
    top: 330px;
    width: 460px;
    height: 510px;
    overflow: hidden;
    background: linear-gradient(180deg, var(--label-brown-dark) 0%, var(--label-brown) 30%, var(--label-brown) 100%);
  }
  .label--classic { left: 95px; border: 1px solid var(--gold-deep); }
  .label--red { left: 645px; }

  .label__band {
    position: absolute;
    left: 0; right: 0;
    height: 15px;
    z-index: 3;
  }
  .label__band--top { top: 0; }
  .label__band--bottom { bottom: 0; }
  .label--classic .label__band { background: linear-gradient(90deg, var(--gold-deep), var(--gold-light) 30%, var(--gold-mid) 60%, var(--gold-light) 85%, var(--gold-deep)); }
  .label--red .label__band { background: linear-gradient(90deg, var(--wine-red-deep), var(--wine-red) 50%, var(--wine-red-deep)); }

  .label__frame {
    position: absolute;
    top: 15px; bottom: 15px; left: 15px; right: 15px;
    border-left: 1px solid var(--gold-deep);
    border-right: 1px solid var(--gold-deep);
    z-index: 2;
  }
  .label--red .label__frame { border-color: var(--wine-red); }

  .brand-mark {
    position: absolute;
    top: 31px;
    left: 50%;
    width: 112px; height: 112px;
    margin-left: -56px;
    border: 2px solid var(--gold-mid);
    border-radius: 50%;
    display: flex;
    align-items: center;
    justify-content: center;
  }
  .label--red .brand-mark { top: 36px; }
  .brand-mark__name {
    font-weight: 700;
    font-size: 10.5px;
    letter-spacing: 0.02em;
    color: var(--gold-light);
  }

  .wine-name {
    position: absolute;
    left: 0; right: 0;
    text-align: center;
    font-weight: 400;
    color: var(--title-gold);
    z-index: 1;
  }
  .wine-name--serif {
    top: 156px;
    font-family: "Libre Caslon Text", serif;
    font-size: 54px;
    line-height: 1;
  }
  .wine-name--caps {
    top: 174px;
    font-family: "Marcellus", serif;
    font-size: 44px;
    line-height: 1;
  }

  .vineyard-scene {
    position: absolute;
    left: 16px; right: 16px;
    top: 212px;
    height: 205px;
    background:
      radial-gradient(ellipse 45% 40% at 50% 72%, rgba(192, 138, 76, 0.55), rgba(192, 138, 76, 0) 100%),
      radial-gradient(ellipse 22% 60% at 8% 45%, rgba(125, 134, 96, 0.7), rgba(125, 134, 96, 0) 100%),
      radial-gradient(ellipse 22% 60% at 92% 45%, rgba(125, 134, 96, 0.7), rgba(125, 134, 96, 0) 100%),
      linear-gradient(180deg, rgba(69, 32, 15, 0) 0%, var(--sky-glow) 16%, var(--field-ochre) 40%, var(--field-ochre) 78%, rgba(69, 32, 15, 0) 100%);
  }

  .grape-variety {
    position: absolute;
    top: 434px;
    left: 0; right: 0;
    text-align: center;
    font-family: "Cinzel", serif;
    font-weight: 600;
    font-size: 17px;
    letter-spacing: 0.03em;
    color: var(--variety-red);
  }
  .vintage {
    position: absolute;
    top: 463px;
    left: 0; right: 0;
    text-align: center;
    font-family: "Libre Caslon Text", serif;
    font-size: 14px;
    letter-spacing: 0.22em;
    color: var(--year-cream);
  }

  .brand-swatch {
    position: absolute;
    left: 9px;
    top: 1083px;
    width: 106px; height: 106px;
    background: var(--label-brown);
    display: flex;
    align-items: center;
    justify-content: center;
  }
  .brand-swatch__ring {
    width: 88px; height: 88px;
    border: 1.5px solid var(--gold-mid);
    border-radius: 50%;
    display: flex;
    align-items: center;
    justify-content: center;
  }
  .brand-swatch__name {
    font-weight: 700;
    font-size: 7.5px;
    color: var(--gold-mid);
  }
</style>
</head>
<body>
  <p class="variant-caption variant-caption--one">Typo 1</p>
  <p class="variant-caption variant-caption--two">Typo 2</p>

  <section class="label label--classic">
    <div class="label__band label__band--top"></div>
    <div class="label__frame"></div>
    <div class="brand-mark"><span class="brand-mark__name">CAL VERDUNES</span></div>
    <div class="vineyard-scene" role="img" aria-label="Engraved vineyard landscape with cypress and pine trees and two teddy bears driving a tractor through the rows"></div>
    <h1 class="wine-name wine-name--serif">Bertoldo</h1>
    <p class="grape-variety">Cabernet Sauvignon</p>
    <p class="vintage">2025</p>
    <div class="label__band label__band--bottom"></div>
  </section>

  <section class="label label--red">
    <div class="label__band label__band--top"></div>
    <div class="label__frame"></div>
    <div class="brand-mark"><span class="brand-mark__name">CAL VERDUNES</span></div>
    <div class="vineyard-scene" role="img" aria-label="Engraved vineyard landscape with cypress and pine trees and two teddy bears driving a tractor through the rows"></div>
    <h1 class="wine-name wine-name--caps">BERTOLDO</h1>
    <p class="grape-variety">Cabernet Sauvignon</p>
    <p class="vintage">2025</p>
    <div class="label__band label__band--bottom"></div>
  </section>

  <div class="brand-swatch">
    <div class="brand-swatch__ring"><span class="brand-swatch__name">CAL VERDUNES</span></div>
  </div>
</body>
</html>
```